SiteForge design for BrisleyTorvane.com

*****
OVERVIEW
*****
BrisleyTorvane.com needs a fresh, clean, professional design that effectively illustrates its talent in a thoughtful, impressive, and impactful way.
Torvane Architecture & Interiors (www.brisleytorvane.com) is a well-established, prestigious, well-publicized New England USA architecture firm. Founded in 1996, the privately-held company specializes in high-end residential projects with a focus on classic New England style architecture.
Business contact information is as noted below:
Address:
Torvane Architecture & Interiors
18 Orchard Street
Welland, MA 02381
Telephone:
617-555-0183
781-555-0147
Email:
info@brisleytorvane.com
An excerpt from the current site describes the outfit with this:
"Our architecture and interior design practices are centered around the philosophy that successful living spaces combine a focus on richly articulated detail and an in-depth knowledge of quality construction techniques."
*****
DESIGN RESEARCH
*****
In reviewing design ideas, the following sites were appealing:
Good
- Marcus Pennow Architects (http://mpwarchitects.example/) - Simple and clean, but almost too simple.
Better
- Garvin Stroud Architecture (http://www.garvinstroud.example/) - Direct portfolio access. Simple and clean.
Best
- Bramwell Architects (http://www.bramwellarchitects.example/) - Clean, simple, easy to navigate
- QRT Architecture & Interiors (http://www.qrt-architects.example/) - Excellent use of high-resolution media, transitions, and navigation.
Here is an example of what is NOT desired:
Pembury Sallow Architects (http://www.pemburysallow.example/) - Cluttered, tight landing page. Uncertain navigation.
*****
OTHER DETAILS
*****
The grey in the Torvane Architecture & Interiors logo is hex 636363. The font is unknown.
Updates
Project Deadline Extended
Reason: Hello everyone,
Thank you for your continued patience with this project. As it turns out, a critical member of the decision making team on our client's end has been out of the office this week. She will be back next week and is ready to be fully engaged with this. That said, we are extending the contest for at least 5 days. Next week will be much more active.
Thank you for your understanding.
Cloverpine Technology Services
Project Deadline Extended
Reason: Hello everyone,
The customer was on vacation and only returned Monday of this week. That said, we need to extend the deadline for 5 days to afford time for review and comment.
Thank you for your patience! The designs submitted thus far are fantastic!
Thanks again,
Project Deadline Extended
Reason: Hello,
With so many designs, the customer is taking longer than anticipated to review them. They are looking at them offline and will process a large batch of comments when ready.
That said, the contest is being extended again.
Thank you for your continued patience.
Project Deadline Extended
Reason: Hello,
Because there are 108 designs to review and comment on, this is taking much longer than anticipated. That said, the contest is being extended another 5 days to ensure the customer has the desired outcome.
Thank you,
Target Market(s)
- Would-be clients
- Landowners
- Construction firms and general contractors
- High-end residential component manufacturers
- Media outlets
- All others interested in high-end residential architecture and interior design
Industry/Entity Type
Architecture
Requirements
Must have
- - Lots of media capabilities, such as embedded video (via ViewStream is fine), project image gallery, sliders for various functions, and social media integrations
- - At least one large slider on the landing page is critical, as well as space for standard lead-in things, such as news/events, opportunities, project highlights, and the likes
- - A high-resolution project showcase - finished projects and works in progress - is critical
- - A place to highlight business partners with the potential for reciprocation
- Form capabilities for things like information requests and general contacts from the public
- - Design must be handed off in a logically-layered (for SiteForge) PSD with any and all additional source files provided (e.g. Photoshop, Illustrator, fonts, etc)
Nice to have
- - The SiteForge design should be capable of fitting into the very popular Plumfield Easel theme.

```html
<!DOCTYPE html>
<html lang="en">
<head>
<meta charset="utf-8">
<title>Torvane Architecture &amp; Interiors</title>
<link href="https://fonts.googleapis.com/css2?family=Roboto:wght@300;400;500;700&family=Open+Sans:wght@400;600;700&display=swap" rel="stylesheet">
<style>
:root{
  --brand-grey:#636363;
  --ink:#2f2f2f;
  --muted:#777;
  --rule:#cfcfcf;
  --panel:#ececec;
  --dark:#474747;
  --footer:#4a4a4a;
  --white:#fff;
  --hero-a:#d9d6d0;
  --hero-b:#8d8782;
  --classic-a:#3a3a3a;
  --classic-b:#1f1f1f;
}
*{margin:0;padding:0;box-sizing:border-box}
html,body{width:1200px;height:2768px;overflow:hidden}
body{position:relative;font-family:"Open Sans",Arial,sans-serif;color:var(--ink);background:var(--white)}
h2,h3{font-weight:400}
.abs{position:absolute}

/* hero */
.hero{left:0;top:0;width:1200px;height:760px;background:linear-gradient(135deg,var(--hero-a) 0%,#c6c1ba 45%,var(--hero-b) 100%)}
.site-header{left:0;top:0;width:1200px;height:120px;background:rgba(70,70,70,.55)}
.logo{left:72px;top:22px;color:var(--white);font-family:"Roboto",sans-serif;font-weight:300}
.logo-name{font-size:62px;letter-spacing:5px;line-height:62px}
.logo-sub{font-size:15px;letter-spacing:4px;margin-top:4px}
.main-nav{left:448px;top:30px;display:flex;gap:4px}
.main-nav a{display:block;height:48px;line-height:48px;padding:0 22px;color:var(--white);font-family:"Roboto",sans-serif;font-size:18px;font-weight:500;text-decoration:none}
.main-nav a.active{background:rgba(255,255,255,.85);color:var(--ink)}

/* section headings */
.section-title{left:0;width:1200px;text-align:center;font-family:"Roboto",sans-serif;font-size:48px;font-weight:400;color:var(--ink)}
.section-title span{background:var(--white);padding:0 26px;position:relative}
.title-rule{height:2px;background:var(--rule)}

.intro{left:180px;top:880px;width:840px;text-align:center;font-size:15px;line-height:26px;color:var(--muted)}
.btn{display:block;background:var(--dark);color:var(--white);font-family:"Roboto",sans-serif;font-weight:500;text-align:center;text-decoration:none}
.read-more{left:510px;top:990px;width:180px;height:52px;line-height:52px;font-size:18px}
.figure-spot{left:0;top:968px;width:170px;height:144px;background:linear-gradient(180deg,#bdbdbd,#8a8a8a);z-index:2}

/* simply classic */
.classic{left:0;top:1112px;width:1200px;height:388px;background:linear-gradient(135deg,var(--classic-a),var(--classic-b))}
.classic-title{left:0;top:1150px;width:1200px;text-align:center;font-family:"Roboto",sans-serif;font-size:48px;font-weight:400;color:var(--white)}
.feature{top:1258px;width:240px;text-align:center;color:var(--white);font-family:"Roboto",sans-serif;font-size:32px}
.feature svg{display:block;margin:0 auto 28px}

/* projects */
.tabs{left:80px;top:1632px;width:1040px;height:58px;display:flex}
.tab{flex:1;background:#6b6b6b;color:var(--white);font-family:"Roboto",sans-serif;font-size:22px;font-weight:500;text-align:center;line-height:58px}
.tab.active{background:var(--panel);color:var(--ink);border:2px solid #d4d4d4;border-bottom:none;font-weight:400}
.gallery{left:80px;top:1690px;width:1040px;height:510px;background:var(--panel)}
.tile{width:330px;height:216px}
.tile.sky{background:linear-gradient(180deg,#6f9fd6 0%,#a9c6e6 45%,#6f8f5a 75%,#4e6d3c 100%)}
.tile.dusk{background:linear-gradient(180deg,#2b3f63 0%,#3e4f6b 55%,#2d3a2c 100%)}
.tile-label{display:flex;flex-direction:column;align-items:center;justify-content:center;color:var(--white);font-family:"Roboto",sans-serif;text-align:center}
.tile-label .l1{font-size:28px;margin-bottom:10px}
.tile-label .l2{font-size:18px;line-height:26px}

/* news and quote */
.col-title{font-family:"Roboto",sans-serif;font-size:52px;font-weight:400;color:var(--ink)}
.news{left:80px;top:2316px;width:480px}
.news-item{padding-bottom:14px;margin-bottom:14px;border-bottom:2px solid var(--rule)}
.news-item h3{font-size:16px;font-weight:700;line-height:22px}
.news-item .meta{font-size:12px;color:var(--muted);margin:6px 0}
.news-item p{font-size:14px;line-height:20px;color:#555}
.news-item b{color:var(--ink)}
.divider{left:600px;top:2250px;width:2px;height:340px;background:var(--rule)}
.field{background:#e4e4e4;border:1px solid #d2d2d2;font-size:14px;color:#8a8a8a;padding:0 14px;line-height:36px}
.submit{left:640px;top:2536px;width:120px;height:38px;line-height:38px;font-size:16px}

/* footer */
.site-footer{left:0;top:2640px;width:1200px;height:128px;background:var(--footer)}
.foot-nav{left:76px;top:2660px;display:flex;gap:30px;font-family:"Roboto",sans-serif;font-size:16px;color:var(--white)}
.copyright{left:76px;top:2710px;font-size:14px;color:var(--white)}
.social{left:1026px;top:2712px;display:flex;gap:22px}
.social span{width:18px;height:18px;border-radius:50%;background:var(--white)}
</style>
</head>
<body>

<div class="abs hero" role="img" aria-label="Photo of a bright modern living room with a lounge chair, rug and wall unit"></div>
<header class="abs site-header"></header>
<div class="abs logo">
  <div class="logo-name">TORVANE</div>
  <div class="logo-sub">ARCHITECTURE &amp; INTERIORS</div>
</div>
<nav class="abs main-nav">
  <a class="active" href="#">HOME</a><a href="#">ABOUT</a><a href="#">SERVICES</a><a href="#">RESIDENTIAL</a><a href="#">AFFILIATE</a><a href="#">CONTACT</a>
</nav>

<div class="abs title-rule" style="left:80px;top:860px;width:1040px"></div>
<h2 class="abs section-title" style="top:828px"><span>Welcome to TORVANE</span></h2>
<p class="abs intro">Torvane Architecture &amp; Interiors is a Boston based firm specializing in architecture and interior design for custom residences. Since our inception in 1996, we have designed homes that reflect our reverence for traditional architecture and our commitment to creating a collaborative working relationship with our clients.</p>
<a class="abs btn read-more" href="#">READ MORE</a>
<div class="abs figure-spot" role="img" aria-label="Photo of a business person in a suit leaning in from the left"></div>

<section class="abs classic" role="img" aria-label="Dark photo of a classic interior with fireplace and seating"></section>
<h2 class="abs classic-title">Simply Classic</h2>
<div class="abs feature" style="left:120px">
  <svg width="90" height="90" viewBox="0 0 90 90"><circle cx="45" cy="45" r="40" fill="#fff"/><path d="M45 18V46L62 56" stroke="#2a2a2a" stroke-width="6" fill="none" stroke-linecap="round"/></svg>
  Timeless
</div>
<div class="abs feature" style="left:480px">
  <svg width="90" height="90" viewBox="0 0 90 90" fill="#fff"><g transform="translate(34 48)"><circle r="22"/><g><rect x="-6" y="-31" width="12" height="62"/><rect x="-6" y="-31" width="12" height="62" transform="rotate(45)"/><rect x="-6" y="-31" width="12" height="62" transform="rotate(90)"/><rect x="-6" y="-31" width="12" height="62" transform="rotate(135)"/></g><circle r="8" fill="#2a2a2a"/></g><g transform="translate(70 22)"><circle r="12"/><rect x="-4" y="-18" width="8" height="36"/><rect x="-4" y="-18" width="8" height="36" transform="rotate(60)"/><rect x="-4" y="-18" width="8" height="36" transform="rotate(120)"/><circle r="4" fill="#2a2a2a"/></g></svg>
  Detailed
</div>
<div class="abs feature" style="left:840px">
  <svg width="90" height="90" viewBox="0 0 90 90"><path d="M22 6H60L70 16V84H22Z" fill="#fff"/><path d="M30 30H62M30 42H62M30 54H62M30 66H52" stroke="#2a2a2a" stroke-width="3"/></svg>
  Personal
</div>

<div class="abs title-rule" style="left:80px;top:1604px;width:1040px"></div>
<h2 class="abs section-title" style="top:1572px"><span>Our Projects</span></h2>
<div class="abs tabs">
  <div class="tab active">Architecture</div><div class="tab">Interior Design</div><div class="tab">Renovation &amp; Additions</div>
</div>
<div class="abs gallery"></div>
<div class="abs tile dusk tile-label" style="left:90px;top:1720px" role="img" aria-label="Project photo of a house at dusk">
  <div class="l1">Location :</div><div class="l2">HARWICK - BAYLEY<br>ISLAND #1</div>
</div>
<div class="abs tile sky" style="left:435px;top:1720px" role="img" aria-label="Project photo of a shingled house on a lawn"></div>
<div class="abs tile sky" style="left:780px;top:1720px" role="img" aria-label="Project photo of a white colonial house"></div>
<div class="abs tile sky" style="left:90px;top:1952px" role="img" aria-label="Project photo of a large gabled residence"></div>
<div class="abs tile sky" style="left:435px;top:1952px" role="img" aria-label="Project photo of a house among trees"></div>
<div class="abs tile sky" style="left:780px;top:1952px" role="img" aria-label="Project photo of a house with driveway"></div>

<h2 class="abs col-title" style="left:80px;top:2244px">Latest News</h2>
<div class="abs news">
  <div class="news-item">
    <h3>Lorem Ipsum is simply dummy text of the printing and typesetting industry.</h3>
    <div class="meta">Posted on 16 Oct 2015 by Admin</div>
    <p>Lorem Ipsum is simply dummy text of the printing and typesetting industry. <b>READ MORE</b></p>
  </div>
  <div class="news-item" style="border-bottom:none">
    <h3>Lorem Ipsum is simply dummy text of the printing.</h3>
    <div class="meta">Posted on 16 Oct 2015 by Admin</div>
    <p>Lorem Ipsum is simply dummy text of the printing and typesetting industry. <b>READ MORE</b></p>
  </div>
</div>
<div class="abs divider"></div>
<h2 class="abs col-title" style="left:640px;top:2244px">Get a quote</h2>
<div class="abs field" style="left:640px;top:2318px;width:220px;height:38px">Enter Name</div>
<div class="abs field" style="left:888px;top:2318px;width:232px;height:38px">Enter Email</div>
<div class="abs field" style="left:640px;top:2376px;width:480px;height:38px">Enter Subject</div>
<div class="abs field" style="left:640px;top:2434px;width:480px;height:82px">Enter Message</div>
<a class="abs btn submit" href="#">SUBMIT</a>

<footer class="abs site-footer"></footer>
<nav class="abs foot-nav"><span>Home</span><span>About</span><span>Architecture</span><span>Interior Design</span><span>Works In Progress</span><span>Renovations And Additions</span><span>News</span><span>Affiliates</span><span>Contact</span></nav>
<div class="abs copyright">© TORVANE · 2015. All Rights Reserved.</div>
<div class="abs social"><span></span><span></span><span></span></div>

</body>
</html>
```